Webinar email campaign graphic/template

We need a static email campaign graphic that can be customized for a variety of communications - webinar announcement, whitepaper distribution, etc. Need ability to edit the files for text content. Attached are current examples/format. Please refer to website for design theme/ideas. www.k7cargoledger.com

Target Market(s)

Transportation executives

Industry/Entity Type

All

Requirements
Must have
• Ability to customize text for headers/content
Should not have
• Inability to edit text

```html
<!DOCTYPE html>
<html lang="en">
<head>
<meta charset="utf-8">
<title>K7 Cargo Ledger – Webinar Announcement</title>
<link rel="stylesheet" href="https://fonts.googleapis.com/css2?family=Arimo:wght@400;700&display=swap">
<style>
  :root {
    --navy: #243c78;
    --title-blue: #2a3f8f;
    --ink: #4d4d4d;
    --body: #555555;
    --yellow: #fff200;
    --button-ink: #1f2a44;
    --white: #ffffff;
  }
  * { margin: 0; padding: 0; box-sizing: border-box; }
  html, body { width: 1200px; height: 1200px; overflow: hidden; background: var(--white); }
  body { font-family: "Arimo", Arial, sans-serif; position: relative; }

  .hero { position: absolute; left: 0; top: 0; width: 1200px; height: 330px; }
  .hero svg { display: block; }

  .brand-name {
    position: absolute; left: 64px; top: 74px;
    font-size: 26px; font-weight: 400; color: var(--ink); letter-spacing: -0.3px;
  }

  .hero-title {
    position: absolute; left: 0; width: 1200px; top: 174px;
    text-align: center; font-size: 37px; font-weight: 700;
    color: var(--title-blue); letter-spacing: 0.3px;
  }

  .headline {
    position: absolute; left: 0; width: 1200px; top: 362px;
    text-align: center; font-size: 31px; font-weight: 700; color: var(--ink);
    letter-spacing: 0.2px;
  }

  .intro { position: absolute; left: 64px; top: 469px; width: 540px; }
  .intro-lead { font-size: 22.5px; line-height: 31px; font-weight: 700; color: var(--navy); }
  .intro-body { margin-top: 14px; font-size: 17.5px; line-height: 32.4px; color: var(--body); }

  .details { position: absolute; left: 708px; top: 467px; font-size: 22.5px; line-height: 35px; color: var(--navy); }
  .details strong { font-weight: 700; }

  .register {
    position: absolute; left: 705px; top: 644px; width: 341px; height: 71px;
    background: var(--yellow); color: var(--button-ink);
    display: flex; align-items: center; padding-left: 26px; gap: 12px;
    font-size: 20px; font-weight: 700; text-decoration: none;
    box-shadow: 0 4px 5px rgba(0,0,0,0.25);
  }

  .unsubscribe {
    position: absolute; left: 0; width: 1200px; top: 1140px; text-align: center;
  }
  .unsubscribe a { font-size: 19px; font-weight: 700; color: var(--ink); text-decoration: underline; text-underline-offset: 3px; }
</style>
</head>
<body>
  <header class="hero">
    <svg width="1200" height="330" viewBox="0 0 1200 330" role="img" aria-label="Photo of a container ship stacked with cargo containers at a port with cranes, a truck and an airplane overhead">
      <defs>
        <linearGradient id="heroTones" x1="0" y1="0" x2="1" y2="0">
          <stop offset="0" stop-color="#eef0f6"/>
          <stop offset="0.3" stop-color="#c9d2e6"/>
          <stop offset="0.5" stop-color="#c8737a"/>
          <stop offset="0.7" stop-color="#5f86b8"/>
          <stop offset="0.88" stop-color="#3f5878"/>
          <stop offset="1" stop-color="#2f4a66"/>
        </linearGradient>
        <linearGradient id="heroFade" x1="0" y1="0" x2="0" y2="1">
          <stop offset="0" stop-color="#ffffff" stop-opacity="0.45"/>
          <stop offset="1" stop-color="#ffffff" stop-opacity="0"/>
        </linearGradient>
      </defs>
      <polygon points="0,0 1200,0 1200,218 596,326 0,218" fill="url(#heroTones)"/>
      <polygon points="0,0 1200,0 1200,218 596,326 0,218" fill="url(#heroFade)"/>
    </svg>
    <span class="brand-name">K7 Cargo Ledger</span>
    <h1 class="hero-title">WEBINAR ANNOUNCEMENT</h1>
  </header>

  <h2 class="headline">Best Practices for Auditing Your Freight Payment Provider</h2>

  <section class="intro">
    <p class="intro-lead">K7 Cargo Ledger understands the challenges associated with procuring a freight bill audit and payment solution.</p>
    <p class="intro-body">Drawing on experience from participation in hundreds of freight payment bids, the K7 Cargo Ledger team offers the following advice and resources to assist you with your RFI/RFP efforts. If you are looking for information on a specific topic you don't see listed, please contact us as we frequently update content on this page and may have a reference document related to your interest.</p>
  </section>

  <section class="details">
    <p><strong>Date:</strong> Wednesday, September 15</p>
    <p><strong>Time:</strong> 11:30 Eastern - 12:30 Central</p>
  </section>

  <a class="register" href="#">
    <span>Click Here To Register Now</span>
    <svg width="32" height="14" viewBox="0 0 32 14" aria-hidden="true">
      <path d="M0 7 H29 M23 1.5 L29.5 7 L23 12.5" fill="none" stroke="#1f2a44" stroke-width="2"/>
    </svg>
  </a>

  <footer class="unsubscribe"><a href="#">Click Here to Unsubscribe</a></footer>
</body>
</html>
```